A Web3 (Blockchain) Company need a Web Design

Hi from NineRidgeLabs.
We need a web design for a Blockchain company focused on infrastructure. We are building infrastructure that make people with non-blockchain knowledge and experience can build blockchain platform/service easier.

Our logo will have bridge/road ambience.
We also think about some blue color.
But please propose your idea.

We want the website to represent us in "Reliable", "Secure", and "Make your blockchain related development easier".

I include sales deck to make you understand more about our business.
We expect the design to be in figma.

```html
<!DOCTYPE html>
<html lang="en">
<head>
<meta charset="utf-8">
<title>Web3 Infrastructure Products</title>
<link rel="stylesheet" href="https://fonts.googleapis.com/css2?family=Inter:wght@300;400;500;700&display=swap">
<style>
  :root {
    --band-start: #27497a;
    --band-end: #1a2c4f;
    --dark-bg: #232323;
    --modal-bg: #f4f6f5;
    --ink: #1c1c1c;
    --muted-title: #8d8d8d;
    --muted-text: #7c7c7c;
    --accent-blue: #1b6fd8;
    --check: #efb440;
    --btn-bg: #7e7e7e;
    --btn-text: #1e3d75;
  }
  * { box-sizing: border-box; margin: 0; padding: 0; }
  html, body { width: 1135px; height: 1200px; overflow: hidden; }
  body { font-family: "Inter", Helvetica, Arial, sans-serif; background: var(--dark-bg); }
  .page { position: relative; width: 1135px; height: 1200px; overflow: hidden; background: var(--dark-bg); }

  .hero-band {
    position: absolute; left: 0; top: 0; width: 1135px; height: 585px;
    background: linear-gradient(110deg, var(--band-start) 0%, var(--band-end) 100%);
  }
  .hero-title {
    position: absolute; left: 0; width: 1135px; top: 97px;
    text-align: center; font-size: 33.5px; font-weight: 700; color: var(--muted-title);
  }

  .products { position: absolute; left: 0; top: 0; width: 1135px; height: 1200px; }
  .product { position: absolute; width: 300px; }
  .product-icon { width: 48px; height: 48px; border-radius: 10px; }
  .product-title { margin-top: 21px; font-size: 19px; font-weight: 700; color: var(--muted-title); }
  .product-text { margin-top: 2px; font-size: 12.5px; font-weight: 300; line-height: 17px; color: var(--muted-text); }
  .product-btn {
    position: absolute; left: 0; height: 30px; padding: 0 17px;
    border-radius: 15px; background: var(--btn-bg); color: var(--btn-text);
    font-size: 12px; font-weight: 700; line-height: 30px; white-space: nowrap;
  }

  .modal {
    position: absolute; left: 42px; top: 149px; width: 1052px; height: 569px;
    background: var(--modal-bg); border-radius: 18px;
  }
  .modal-close { position: absolute; left: 992px; top: 27px; }
  .modal-illustration {
    position: absolute; left: 50px; top: 117px; width: 430px; height: 316px;
    border-radius: 50%;
    background: radial-gradient(ellipse at 55% 55%, #c9c8f2 0%, #dedcf8 55%, #eceaf9 80%, rgba(244,246,245,0) 100%);
  }
  .modal-heading { position: absolute; left: 525px; top: 130px; font-size: 33.7px; font-weight: 700; color: var(--ink); letter-spacing: -0.2px; }
  .modal-sub { position: absolute; left: 525px; top: 176px; font-size: 18.9px; color: var(--ink); }
  .feature-list { position: absolute; left: 525px; top: 228px; list-style: none; }
  .feature-list li { display: flex; align-items: center; height: 46.6px; font-size: 18.7px; color: var(--ink); }
  .feature-list svg { margin-right: 13px; flex: none; }
  .modal-quote {
    position: absolute; left: 0; width: 1052px; top: 480px; text-align: center;
    font-size: 19.5px; font-weight: 700; color: var(--accent-blue);
  }
</style>
</head>
<body>
<div class="page">
  <div class="hero-band">
    <h1 class="hero-title">Indonesia’s Web 3.0 Project Obstacles</h1>
  </div>

  <section class="products">
    <div class="product" style="left:94px; top:729px;">
      <div class="product-icon" role="img" aria-label="Wallet icon" style="background:linear-gradient(160deg,#5b7ea8,#b08a3a);"></div>
      <h2 class="product-title">Whitelabel Web3 Wallet</h2>
      <p class="product-text">Let you focus on your businesses.</p>
      <span class="product-btn" style="top:139px;">Read More</span>
    </div>
    <div class="product" style="left:434px; top:729px;">
      <div class="product-icon" role="img" aria-label="NFT starter icon" style="background:linear-gradient(160deg,#3a6c9a,#a88436);"></div>
      <h2 class="product-title">NFT Starter</h2>
      <p class="product-text">Create and launch your NFT with ease.</p>
      <span class="product-btn" style="top:139px;">Read More</span>
    </div>
    <div class="product" style="left:775px; top:729px; width:340px;">
      <div class="product-icon" role="img" aria-label="Soulbound token icon" style="background:linear-gradient(160deg,#2f7fa5,#a8893a);"></div>
      <h2 class="product-title">Soulbound Token</h2>
      <p class="product-text">Easier approach to create a soulbound token.</p>
      <span class="product-btn" style="top:139px;">Coming Soon</span>
    </div>

    <div class="product" style="left:94px; top:953px;">
      <div class="product-icon" role="img" aria-label="RPC nodes icon" style="background:linear-gradient(160deg,#3d5f9a,#a88436);"></div>
      <h2 class="product-title">RPC Nodes</h2>
      <p class="product-text">With RPC nodes, makes your transaction<br>faster and more reliable.</p>
      <span class="product-btn" style="top:156px;">Read More</span>
    </div>
    <div class="product" style="left:434px; top:953px;">
      <div class="product-icon" role="img" aria-label="Blockchain API shield icon" style="background:linear-gradient(160deg,#2b3e6a,#a88436);"></div>
      <h2 class="product-title">Blockchain API</h2>
      <p class="product-text">Makes your token development easier,<br>develop web3 project with web2 knowledge.</p>
      <span class="product-btn" style="top:155px;">Read More</span>
    </div>
    <div class="product" style="left:775px; top:953px;">
      <div class="product-icon" role="img" aria-label="Sandbox laptop icon" style="background:linear-gradient(160deg,#2f6a9a,#a88436);"></div>
      <h2 class="product-title">Web3 Sandbox</h2>
      <p class="product-text">Web3 Sanbox makes your smart contract<br>development smoother.</p>
      <span class="product-btn" style="top:155px;">Read More</span>
    </div>
  </section>

  <div class="modal">
    <svg class="modal-close" width="30" height="30" viewBox="0 0 30 30" fill="none">
      <circle cx="15" cy="15" r="13" stroke="#444" stroke-width="2"/>
      <path d="M10.5 10.5 L19.5 19.5 M19.5 10.5 L10.5 19.5" stroke="#444" stroke-width="2.2" stroke-linecap="round"/>
    </svg>
    <div class="modal-illustration" role="img" aria-label="Illustration of a woman in a yellow jacket pointing at a phone sending crypto coins to a wallet, over a lavender city backdrop"></div>
    <h2 class="modal-heading">Whitelabel Web3 Wallet</h2>
    <p class="modal-sub">Let you focus on your businesses.</p>
    <ul class="feature-list">
      <li><svg width="21" height="21" viewBox="0 0 21 21" fill="none"><path d="M18 8.5 A8.5 8.5 0 1 1 14 3" stroke="var(--check)" stroke-width="2" stroke-linecap="round"/><path d="M6.5 10 L9.5 13 L19 3.5" stroke="var(--check)" stroke-width="2" stroke-linecap="round" stroke-linejoin="round"/></svg>Familiar User Interface</li>
      <li><svg width="21" height="21" viewBox="0 0 21 21" fill="none"><path d="M18 8.5 A8.5 8.5 0 1 1 14 3" stroke="var(--check)" stroke-width="2" stroke-linecap="round"/><path d="M6.5 10 L9.5 13 L19 3.5" stroke="var(--check)" stroke-width="2" stroke-linecap="round" stroke-linejoin="round"/></svg>Safe Non-Custodial Type</li>
      <li><svg width="21" height="21" viewBox="0 0 21 21" fill="none"><path d="M18 8.5 A8.5 8.5 0 1 1 14 3" stroke="var(--check)" stroke-width="2" stroke-linecap="round"/><path d="M6.5 10 L9.5 13 L19 3.5" stroke="var(--check)" stroke-width="2" stroke-linecap="round" stroke-linejoin="round"/></svg>Passwords and OTP codes</li>
      <li><svg width="21" height="21" viewBox="0 0 21 21" fill="none"><path d="M18 8.5 A8.5 8.5 0 1 1 14 3" stroke="var(--check)" stroke-width="2" stroke-linecap="round"/><path d="M6.5 10 L9.5 13 L19 3.5" stroke="var(--check)" stroke-width="2" stroke-linecap="round" stroke-linejoin="round"/></svg>Perform perfectly the same as other Web3 Wallet</li>
    </ul>
    <p class="modal-quote">“skip the learning curve and get to the good part”</p>
  </div>
</div>
</body>
</html>
```